UI for Online Code Editor

I need a UI design for an online code editor called Quillworth.

Quillworth is an online code editor for web developers, that aims to be an intuitive and beautiful editor that you can use on any device or browser. The current prototype can be viewed at http://quillworth.example/editor

I am completely open to different colours and UI approaches, feel free to invent a new way for people to code :)

The final design should be something that is clean, elegant and functional. I will favour designs that are genuinely nice to look at and have a 'mac app' polished feel to them.

I have uploaded a psd that will provide a basic idea.

Go crazy, All ideas will be considered.

Target Market(s)

Web Developers

Industry/Entity Type

Online

Requirements
Must have
• -Tabs: similar to vantor tabs, for different files.
-Line numbers
-The editor text area
Nice to have
• -An expandable/contractible file manager, on either side of the editor.
-Related files area under tabs. This is for quick access to files that have been included in the users code (ie jquery.js, etc). This will likely be expandable/contractable.

```html
<!DOCTYPE html>
<html lang="en">
<head>
<meta charset="utf-8">
<title>Quillworth – Online Code Editor</title>
<link href="https://fonts.googleapis.com/css2?family=Open+Sans:wght@300;400;600;700&family=Cousine&display=swap" rel="stylesheet">
<style>
  :root {
    --sidebar-bg: #3a3a3a;
    --sidebar-top: #343434;
    --sidebar-line: #262626;
    --sidebar-text: #dcdcdc;
    --search-bg: #232323;
    --search-text: #8a8a8a;
    --folder-blue: #4f8fd6;
    --tabbar-top: #3b86d6;
    --tabbar-bottom: #1f5fae;
    --tab-active: #f2f2f2;
    --tab-idle: #cdd6e1;
    --tab-text: #555;
    --subbar-bg: #ececec;
    --subbar-line: #d2d2d2;
    --pill-bg: #d6d6d6;
    --gutter-bg: #f0f0f0;
    --gutter-text: #9a9a9a;
    --code-bg: #ffffff;
    --code-text: #2b2b2b;
    --settings-bg: #2f2f2f;
    --settings-text: #e6e6e6;
    --settings-head: #b5b5b5;
    --field-bg: #202020;
    --field-text: #6d6d6d;
    --logo-mark: #3a8ee0;
  }
  * { box-sizing: border-box; margin: 0; padding: 0; }
  html, body { width: 1200px; height: 550px; overflow: hidden; background: var(--sidebar-bg); }
  .app { position: relative; width: 1200px; height: 550px; font-family: "Open Sans", Arial, sans-serif; }

  /* File manager */
  .files { position: absolute; left: 0; top: 0; width: 222px; height: 550px; background: var(--sidebar-bg); }
  .brand { height: 65px; background: var(--sidebar-top); border-bottom: 1px solid var(--sidebar-line); box-shadow: 0 1px 0 #444; position: relative; }
  .brand-mark { position: absolute; left: 30px; top: 23px; width: 20px; height: 20px; background: var(--logo-mark); }
  .brand-name { position: absolute; left: 62px; top: 16px; font-size: 23px; font-weight: 400; color: #fff; letter-spacing: .2px; }
  .search { position: absolute; left: 22px; top: 81px; width: 178px; height: 24px; border-radius: 12px; background: var(--search-bg); box-shadow: inset 0 1px 2px #111, 0 1px 0 #4a4a4a; }
  .search span { position: absolute; left: 14px; top: 4px; font-size: 11px; color: var(--search-text); }
  .search svg { position: absolute; right: 10px; top: 6px; }
  .tree { position: absolute; left: 0; top: 124px; list-style: none; font-size: 11px; color: var(--sidebar-text); }
  .tree li { position: relative; height: 24.3px; }
  .tree .twisty { position: absolute; left: 32px; top: 7px; }
  .tree .folder-icon { position: absolute; left: 47px; top: 5px; }
  .tree .label { position: absolute; top: 4px; white-space: nowrap; }
  .tree .folder .label { left: 69px; }
  .tree .doc .label { left: 84px; }
  .tree .doc-icon { position: absolute; left: 64px; top: 4px; }

  /* Editor */
  .editor { position: absolute; left: 222px; top: 0; width: 735px; height: 550px; background: var(--code-bg); }
  .tabbar { position: relative; height: 35px; background: linear-gradient(var(--tabbar-top), var(--tabbar-bottom)); }
  .tab { position: absolute; top: 7px; height: 28px; border-radius: 7px 7px 0 0; background: var(--tab-idle); font-size: 12px; color: var(--tab-text); text-align: center; line-height: 28px; }
  .tab.is-active { background: var(--tab-active); font-weight: 600; color: #666; }
  .tab-add { position: absolute; left: 262px; top: 8px; color: #fff; font-size: 20px; font-weight: 700; }
  .expand { position: absolute; right: 8px; top: 7px; }
  .related { position: relative; height: 31px; background: var(--subbar-bg); border-bottom: 1px solid var(--subbar-line); }
  .related-label { position: absolute; left: 24px; top: 9px; font-size: 10px; color: #666; }
  .related-file { position: absolute; left: 89px; top: 5px; width: 66px; height: 20px; border-radius: 10px; background: var(--pill-bg); font-size: 10.5px; color: #444; text-align: center; line-height: 20px; }
  .view-btn { position: absolute; top: 4px; width: 24px; height: 23px; border: 1px solid #c4c4c4; border-radius: 3px; background: linear-gradient(#fafafa, #e2e2e2); }
  .view-btn svg { position: absolute; left: 4px; top: 4px; }
  .code { position: absolute; left: 0; top: 66px; width: 735px; height: 484px; }
  .gutter { position: absolute; left: 0; top: 0; width: 28px; height: 484px; background: var(--gutter-bg); border-right: 1px solid #e4e4e4; }
  .lines { position: absolute; left: 0; top: 2px; width: 735px; list-style: none; font-family: "Cousine", "Courier New", monospace; font-size: 9.8px; }
  .lines li { position: relative; height: 16.43px; line-height: 16.43px; }
  .lines .num { position: absolute; left: 0; width: 28px; text-align: center; color: var(--gutter-text); font-size: 9px; }
  .lines .src { position: absolute; left: 39px; white-space: pre; color: var(--code-text); }

  /* Settings */
  .settings { position: absolute; left: 957px; top: 0; width: 243px; height: 550px; background: var(--settings-bg); color: var(--settings-text); }
  .settings-head { position: absolute; left: 24px; top: 9px; font-size: 12.5px; font-weight: 700; color: var(--settings-head); letter-spacing: .3px; }
  .settings-head svg { vertical-align: -2px; margin-right: 5px; }
  .options { position: absolute; left: 23px; top: 44px; list-style: none; font-size: 10.5px; }
  .options li { height: 22.5px; line-height: 22.5px; white-space: nowrap; }
  .swatch { display: inline-block; width: 20px; height: 11px; background: #fff; vertical-align: -1px; margin-left: 5px; }
  .check { display: inline-block; width: 11px; height: 11px; background: #f1f1f1; border-radius: 2px; vertical-align: -1px; margin: 0 3px 0 5px; position: relative; }
  .check svg { position: absolute; left: 1px; top: 1px; }
  .options .sep { margin: 0 7px; }
  .options .ico { vertical-align: -1px; margin-right: 4px; }
  .divider { position: absolute; left: 23px; top: 305px; width: 197px; height: 1px; background: #222; box-shadow: 0 1px 0 #3d3d3d; }
  .inject { position: absolute; left: 23px; width: 197px; height: 102px; background: var(--field-bg); border-radius: 3px; box-shadow: inset 0 1px 3px #111; font-size: 10px; color: var(--field-text); padding: 8px 10px; }
</style>
</head>
<body>
<div class="app">

  <aside class="files">
    <div class="brand">
      <div class="brand-mark"></div>
      <div class="brand-name">Quillworth</div>
    </div>
    <div class="search">
      <span>Quick Search</span>
      <svg width="12" height="12" viewBox="0 0 12 12"><circle cx="5" cy="5" r="3.8" fill="none" stroke="#fff" stroke-width="1.6"/><line x1="7.8" y1="7.8" x2="11" y2="11" stroke="#fff" stroke-width="1.8"/></svg>
    </div>
    <ul class="tree">
      <li class="folder">
        <svg class="twisty" width="7" height="8" viewBox="0 0 7 8"><path d="M0 0L7 4L0 8Z" fill="#9a9a9a"/></svg>
        <svg class="folder-icon" width="17" height="13" viewBox="0 0 17 13"><path d="M0 1.5Q0 0 1.5 0H6L7.5 2H15.5Q17 2 17 3.5V11.5Q17 13 15.5 13H1.5Q0 13 0 11.5Z" fill="var(--folder-blue)"/></svg>
        <span class="label">Folder 1</span>
      </li>
      <li class="folder">
        <svg class="twisty" width="7" height="8" viewBox="0 0 7 8"><path d="M0 0L7 4L0 8Z" fill="#9a9a9a"/></svg>
        <svg class="folder-icon" width="17" height="13" viewBox="0 0 17 13"><path d="M0 1.5Q0 0 1.5 0H6L7.5 2H15.5Q17 2 17 3.5V11.5Q17 13 15.5 13H1.5Q0 13 0 11.5Z" fill="var(--folder-blue)"/></svg>
        <span class="label">Folder 2</span>
      </li>
      <li class="folder">
        <svg class="twisty" width="8" height="7" viewBox="0 0 8 7"><path d="M0 0H8L4 7Z" fill="#9a9a9a"/></svg>
        <svg class="folder-icon" width="17" height="13" viewBox="0 0 17 13"><path d="M0 1.5Q0 0 1.5 0H6L7.5 2H15.5Q17 2 17 3.5V11.5Q17 13 15.5 13H1.5Q0 13 0 11.5Z" fill="var(--folder-blue)"/></svg>
        <span class="label">Folder 3</span>
      </li>
      <li class="doc">
        <svg class="doc-icon" width="12" height="15" viewBox="0 0 12 15"><path d="M0 0H8L12 4V15H0Z" fill="#eeeeee"/><path d="M8 0V4H12Z" fill="#bbbbbb"/></svg>
        <span class="label">Document 1.html</span>
      </li>
      <li class="doc">
        <svg class="doc-icon" width="12" height="15" viewBox="0 0 12 15"><path d="M0 0H8L12 4V15H0Z" fill="#e9a23b"/><path d="M8 0V4H12Z" fill="#b9741a"/><rect x="2" y="7" width="8" height="5" fill="#fff3d6"/></svg>
        <span class="label">Document 2.jpg</span>
      </li>
    </ul>
  </aside>

  <main class="editor">
    <nav class="tabbar">
      <div class="tab is-active" style="left:10px;width:74px;">Untitled*</div>
      <div class="tab" style="left:88px;width:84px;">Index.html</div>
      <div class="tab" style="left:175px;width:76px;">FAQ.html</div>
      <div class="tab-add">+</div>
      <svg class="expand" width="18" height="18" viewBox="0 0 18 18"><path d="M10 1H17V8L14.5 5.5L11 9L9 7L12.5 3.5Z M8 17H1V10L3.5 12.5L7 9L9 11L5.5 14.5Z" fill="#8fd0ff"/></svg>
    </nav>
    <div class="related">
      <span class="related-label">Source Code</span>
      <span class="related-file">Style.css</span>
      <div class="view-btn" style="left:641px;"><svg width="14" height="14" viewBox="0 0 14 14"><rect x="2" y="1" width="10" height="12" fill="none" stroke="#777"/><path d="M6 5L4.5 7L6 9M8 5L9.5 7L8 9" fill="none" stroke="#777"/></svg></div>
      <div class="view-btn" style="left:674px;"><svg width="16" height="14" viewBox="0 0 16 14"><rect x="0.5" y="1.5" width="8" height="6" fill="none" stroke="#777"/><rect x="6.5" y="6.5" width="8" height="6" fill="#ddd" stroke="#777"/></svg></div>
      <div class="view-btn" style="left:706px;"><svg width="16" height="14" viewBox="0 0 16 14"><rect x="0" y="3" width="10" height="8" rx="1" fill="#777"/><path d="M10 7L15 3V11Z" fill="#777"/></svg></div>
    </div>
    <section class="code">
      <div class="gutter"></div>
      <ol class="lines">
        <li><span class="num">1</span><span class="src">&lt;!DOCTYPE html&gt;</span></li>
        <li><span class="num">2</span><span class="src">  &lt;html id="container-site" class="no-responsive nav-bar-sp-item"&gt;</span></li>
        <li><span class="num">3</span><span class="src">  &lt;head id="ctl00_Head1"&gt;</span></li>
        <li><span class="num">4</span><span class="src"></span></li>
        <li><span class="num">5</span><span class="src">      &lt;script type="text/javascript"&gt;&lt;/script&gt;</span></li>
        <li><span class="num">6</span><span class="src">      &lt;meta charset="utf-8" /&gt;&lt;meta name="viewport" content="width=device-width, initial-scale=1.0" /&gt;&lt;meta name="-</span></li>
        <li><span class="num">7</span><span class="src">      geo.country" content="EU" /&gt;</span></li>
        <li><span class="num">8</span><span class="src"></span></li>
        <li><span class="num">9</span><span class="src">      &lt;!--[if lt IE 9]&gt;&lt;script type="text/javascript" src="//cdn.harborlane.example/common/js/v3/d-</span></li>
        <li><span class="num">10</span><span class="src">      c_ie_300_20130305_1630.js"&gt;&lt;/script&gt;</span></li>
        <li><span class="num">11</span><span class="src">  &lt;![endif]--&gt;</span></li>
        <li><span class="num">12</span><span class="src"></span></li>
        <li><span class="num">13</span><span class="src">      &lt;link rel="stylesheet" href="//cdn.harborlane.example/common/css/v3/dc_20130809_1601.css" /&gt;</span></li>
        <li><span class="num">14</span><span class="src"></span></li>
        <li><span class="num">15</span><span class="src">      &lt;link rel="stylesheet" href="//cdn.harborlane.example/common/css/v3/dc_compatible_20130718_1424.css" /&gt;</span></li>
        <li><span class="num">16</span><span class="src"></span></li>
        <li><span class="num">17</span><span class="src">      &lt;!--[if lt IE 9]&gt;&lt;link rel="stylesheet" href="//cdn.harborlane.example/common/css/v3/d-</span></li>
        <li><span class="num">18</span><span class="src">      c_ie_301_20130711_1837.css" /&gt;</span></li>
        <li><span class="num">19</span><span class="src">  &lt;![endif]--&gt;</span></li>
        <li><span class="num">20</span><span class="src"></span></li>
        <li><span class="num">21</span><span class="src">      &lt;title&gt;</span></li>
        <li><span class="num">22</span><span class="src">     UI for Online Code Editor | Web Design | Harborlane</span></li>
        <li><span class="num">23</span><span class="src">  &lt;/title&gt;&lt;link rel="shortcut icon" href="//cdn.harborlane.example/common/images/v3/favicon.ico" /&gt;&lt;link rel="ap-</span></li>
        <li><span class="num">24</span><span class="src">  ple-touch-icon-precomposed" sizes="144x144" href="//cdn.harborlane.example/common/images/v3/ap-</span></li>
        <li><span class="num">25</span><span class="src"></span></li>
        <li><span class="num">26</span><span class="src"></span></li>
        <li><span class="num">27</span><span class="src"></span></li>
        <li><span class="num">28</span><span class="src"></span></li>
        <li><span class="num">29</span><span class="src"></span></li>
      </ol>
    </section>
  </main>

  <aside class="settings">
    <div class="settings-head">
      <svg width="13" height="13" viewBox="0 0 14 14"><g fill="#b5b5b5"><circle cx="7" cy="7" r="4.6"/><rect x="6" y="0" width="2" height="14"/><rect x="0" y="6" width="14" height="2"/><rect x="6" y="0" width="2" height="14" transform="rotate(45 7 7)"/><rect x="6" y="0" width="2" height="14" transform="rotate(-45 7 7)"/></g><circle cx="7" cy="7" r="2" fill="#2f2f2f"/></svg>SETTINGS
    </div>
    <ul class="options">
      <li>Editor bg colour: <span class="swatch"></span></li>
      <li>Shortcuts:</li>
      <li>Font - size, family, space</li>
      <li>Tab indentation:</li>
      <li>Line Wrapping: <span class="check"><svg width="9" height="9" viewBox="0 0 9 9"><path d="M1 4.5L3.5 7L8 1.5" fill="none" stroke="#555" stroke-width="1.5"/></svg></span></li>
      <li>Live Reload</li>
      <li>Auto Update <span class="check"></span> Off = Ctrl + S to save</li>
      <li>Solarized Theme <span class="check"></span></li>
      <li>Zen cheatsheat</li>
      <li><svg class="ico" width="11" height="11" viewBox="0 0 11 11"><rect x="0.5" y="1.5" width="9" height="9" fill="none" stroke="#e6e6e6"/><path d="M4 7L4.5 5L9 0.5L10.5 2L6 6.5Z" fill="#e6e6e6"/></svg>Edit<span class="sep">|</span><svg class="ico" width="11" height="11" viewBox="0 0 11 11"><rect x="0.5" y="1.5" width="9" height="9" fill="none" stroke="#e6e6e6"/><path d="M6 0H11V5L9.3 3.3L6 6.6L4.4 5L7.7 1.7Z" fill="#e6e6e6"/></svg>Debug in new tab</li>
      <li>Design window</li>
    </ul>
    <div class="divider"></div>
    <div class="inject" style="top:318px;">/* Inject css */</div>
    <div class="inject" style="top:432px;">/* Inject js */</div>
  </aside>

</div>
</body>
</html>
```